IT Network Consultancy - Business Card

kelbrin systems is a IT network consultancy based in London. We're looking for a smart, modern and professional business card design. Our website is here: www.kelbrinsystems.co.uk

Key things that should be included on the card (with examples):

Company Logo
Name
Position / Job Title: Network Consultant
Mobile Phone Number: +44 (0) 7700 900418
Land Line: +44 (0) 1632 960735
Email Address: name@kelbrinsystems.co.uk
Web Site URL: www.kelbrinsystems.co.uk

Target Market(s)

Large enterprise / global companies / corporates

Industry/Entity Type

Business

Requirements
Must have
• Incorporate our logo - which is attached to the project. They are in AI format (can be opened in Inkscape).

The design should be double sided and fit on a UK standard 85mm × 55mm card and be in a format that retains the quality when printed.
Nice to have
• The project does not have to conform to the colour of our website but this should give you inspiration of the style we like.
Should not have
• Bright colours. Pictures are not necessary.

```html
<!DOCTYPE html>
<html lang="en">
<head>
<meta charset="utf-8">
<title>kelbrin systems – Business Card</title>
<link href="https://fonts.googleapis.com/css2?family=Jost:wght@300;400;500;600&display=swap" rel="stylesheet">
<style>
  :root {
    --page: #ffffff;
    --card-light: #ffffff;
    --card-light-shade: #eef0f2;
    --slate-light: #5f6f7b;
    --slate-mid: #4a5964;
    --slate-dark: #2f3a43;
    --teal: #2f5f73;
    --ink: #3b464e;
    --wordmark-grey: #48545c;
    --rule: #8f9ca6;
    --white: #ffffff;
  }
  * { margin: 0; padding: 0; box-sizing: border-box; }
  html, body {
    width: 1200px; height: 900px; overflow: hidden;
    background: var(--page);
    font-family: "Jost", "Futura", sans-serif;
  }
  .canvas { position: relative; width: 1200px; height: 900px; }

  .card {
    position: absolute; top: 296px;
    width: 500px; height: 313px;
    overflow: hidden;
    box-shadow: 2px 3px 5px rgba(0,0,0,0.35);
  }

  /* Front */
  .card--front {
    left: 84px;
    background: radial-gradient(ellipse at 30% 35%, var(--card-light) 40%, var(--card-light-shade) 100%);
  }
  .wordmark {
    position: absolute;
    font-weight: 300;
    text-transform: uppercase;
    letter-spacing: 1px;
    white-space: nowrap;
  }
  .card--front .wordmark {
    left: 38px; top: 30px;
    font-size: 27px;
    color: var(--wordmark-grey);
  }
  .title-block {
    position: absolute; left: 261px; top: 120px;
    width: 229px; height: 36px;
  }
  .title-block::before, .title-block::after {
    content: ""; position: absolute; left: 0; right: 0; height: 1px;
    background: linear-gradient(to right, rgba(143,156,166,0), var(--rule) 45%, rgba(143,156,166,0));
  }
  .title-block::before { top: 0; }
  .title-block::after { bottom: 0; }
  .person-name {
    position: absolute; right: 35px; top: 126px;
    font-size: 18px; font-weight: 600; color: var(--teal);
    white-space: nowrap;
  }
  .person-role {
    position: absolute; right: 35px; top: 157px;
    font-size: 13px; font-weight: 400; color: var(--ink);
  }
  .contact-list {
    position: absolute; left: 30px; top: 195px;
    list-style: none;
    font-size: 14px; line-height: 18px; color: var(--ink);
  }
  .contact-list b { color: var(--teal); font-weight: 600; display: inline-block; width: 19px; }
  .web-band {
    position: absolute; left: 0; bottom: 0; width: 100%; height: 44px;
    background: linear-gradient(to bottom, var(--slate-mid), var(--slate-light));
    color: var(--white);
    font-size: 16px; font-weight: 400;
    text-align: center; line-height: 40px;
  }

  /* Back */
  .card--back {
    left: 619px;
    background: linear-gradient(to bottom, var(--slate-light) 0%, var(--slate-dark) 38%, var(--slate-dark) 62%, var(--slate-light) 100%);
  }
  .logo-band {
    position: absolute; left: 0; top: 120px; width: 100%; height: 72px;
    background: var(--slate-dark);
  }
  .logo-band::before, .logo-band::after {
    content: ""; position: absolute; left: 0; right: 0; height: 1px;
    background: linear-gradient(to right, rgba(255,255,255,0.1), rgba(255,255,255,0.6) 50%, rgba(255,255,255,0.1));
  }
  .logo-band::before { top: 0; }
  .logo-band::after { bottom: 0; }
  .card--back .wordmark {
    left: 0; right: 0; top: 13px; text-align: center;
    font-size: 34px; color: var(--white);
  }
</style>
</head>
<body>
<main class="canvas">
  <section class="card card--front" aria-label="Card front">
    <div class="wordmark">kelbrin systems</div>
    <div class="title-block"></div>
    <div class="person-name">Daniel Marsh</div>
    <div class="person-role">Network Consultant</div>
    <ul class="contact-list">
      <li><b>p.</b>+44 (0) 1632 960735</li>
      <li><b>m.</b>+44 (0) 7700 900418</li>
      <li><b>e.</b>danielmarsh@kelbrinsystems.co.uk</li>
    </ul>
    <div class="web-band">www.kelbrinsystems.co.uk</div>
  </section>

  <section class="card card--back" aria-label="Card back">
    <div class="logo-band">
      <div class="wordmark">kelbrin systems</div>
    </div>
  </section>
</main>
</body>
</html>
```